Harbor of rest- We lessen the Burden

The Harbor of rest is trifold mailer. I have all but the inside of the brochure done. the front and back are designed, just not the middle. I want a testimonial that has the same background feel as the rest of the piece. I did not change the size on the art piece yet, but it will be 8.75*8.75 inches when it's folded. the piece I need you to work on is just 1 side that is 8.75*8.75. Here is the testimonial. (header)- Above Service, Beyond Compassion. (body)-“The fact that you have been trained to work with people in crisis, and that you did this of your own accord, only proves to me your
dedication and commitment to the communities we serve. When
I leave the scene of an accident or death, I know that I am leaving
the victim and their family in capable and understanding hands.”
– Doreen Lyle Hatcher
Calloway Parish Sheriff’s Office

Target Market(s)

funeral homes

Colors

Designer to choose colors to be used in the design.

Requirements
Must have
• The fonts that are used in the uploaded files. The concept of this piece is the Harbor of rest. I placed colored seeds on the second picture. So if a background picture is used, then I'd like it to incorporate these concepts of rebirth and continuous life-cycle
Nice to have
• Compassionate feel through the piece
Should not have
• abrasive yellow. More so the blues and purples

```html
<!DOCTYPE html>
<html lang="en">
<head>
<meta charset="utf-8">
<title>Harbor of rest – Testimonial Panel</title>
<link rel="stylesheet" href="https://fonts.googleapis.com/css2?family=Cormorant+Garamond:ital,wght@1,500;1,600&family=Roboto:ital,wght@0,700;1,500&display=swap">
<style>
  :root {
    --backdrop: #e4e5e7;
    --panel-top: #eef1f5;
    --panel-mid: #c9d7e8;
    --panel-bottom: #a4bddb;
    --navy: #0f2a5c;
    --ink: #2b2b2b;
    --emblem: rgba(74, 120, 180, 0.35);
  }
  * { margin: 0; padding: 0; box-sizing: border-box; }
  html, body {
    width: 1200px;
    height: 1000px;
    overflow: hidden;
    background: var(--backdrop);
  }
  .panel {
    position: absolute;
    left: 190px;
    top: 70px;
    width: 860px;
    height: 860px;
    background: linear-gradient(180deg, var(--panel-top) 0%, var(--panel-mid) 45%, var(--panel-bottom) 100%);
    overflow: hidden;
  }
  .emblem-center {
    position: absolute;
    left: 297px;
    top: 245px;
    width: 340px;
    height: 340px;
    border-radius: 50%;
    background: radial-gradient(circle, var(--emblem) 0%, rgba(74,120,180,0.18) 55%, rgba(74,120,180,0) 72%);
  }
  .emblem-foot {
    position: absolute;
    left: 300px;
    top: 650px;
    width: 300px;
    height: 210px;
    border-radius: 50% 50% 0 0;
    background: radial-gradient(ellipse at 50% 45%, rgba(60,110,180,0.45) 0%, rgba(60,110,180,0.2) 55%, rgba(60,110,180,0) 75%);
  }
  .headline-rule {
    position: absolute;
    left: 45px;
    width: 795px;
    height: 2px;
    background: var(--navy);
  }
  .headline-rule.top { top: 60px; }
  .headline-rule.bottom { top: 145px; }
  .headline {
    position: absolute;
    left: 0;
    top: 68px;
    width: 885px;
    text-align: center;
    font-family: "Cormorant Garamond", serif;
    font-style: italic;
    font-weight: 600;
    font-size: 54px;
    line-height: 74px;
    color: var(--navy);
  }
  .quote {
    position: absolute;
    left: 40px;
    top: 210px;
    width: 805px;
    text-align: center;
    font-family: "Cormorant Garamond", serif;
    font-style: italic;
    font-weight: 500;
    font-size: 34px;
    line-height: 49px;
    color: var(--ink);
  }
  .quote span { display: block; }
  .attribution {
    position: absolute;
    left: 0;
    top: 697px;
    width: 885px;
    text-align: center;
    font-family: "Roboto", sans-serif;
    color: var(--ink);
  }
  .attribution-name {
    font-weight: 700;
    font-size: 26px;
    line-height: 32px;
  }
  .attribution-office {
    font-style: italic;
    font-weight: 500;
    font-size: 17px;
    line-height: 20px;
  }
</style>
</head>
<body>
  <section class="panel">
    <div class="emblem-center" role="img" aria-label="Faint swirling rebirth emblem behind the quote"></div>
    <div class="emblem-foot" role="img" aria-label="Faint tree of life illustration behind the attribution"></div>

    <div class="headline-rule top"></div>
    <h1 class="headline">Above Service, Beyond Compassion</h1>
    <div class="headline-rule bottom"></div>

    <blockquote class="quote">
      <span>“The fact that you have been trained to work</span>
      <span>with people in crisis,</span>
      <span>and that you did this of your own accord,</span>
      <span>only proves to me your dedication and</span>
      <span>commitment to the communities we serve.</span>
      <span>When I leave the scene of an accident or death,</span>
      <span>I know that I am leaving</span>
      <span>the victim and their family in capable and</span>
      <span>understanding hands.”</span>
    </blockquote>

    <div class="attribution">
      <p class="attribution-name">– Doreen Lyle Hatcher –</p>
      <p class="attribution-office">Calloway Parish Sheriff’s Office</p>
    </div>
  </section>
</body>
</html>
```